KT Prime Motion personal training needs a new Business Card design for 2016

Business Card design:
Our current business card is very plain
We are bringing on our first team member next year and thought its a perfect time to have a new face lift for our company!

We are a Personal Training business "KT Prime Motion" who specializes in strength and conditioning / weightloss training,
We also run a yearly Bootcamp called "Ferocity Drillcamps", this is our Logo Design which we are looking for

The pink and blue in the logo are our business colours, how ever we don't want those colours to heavily dominate the card.

We are looking for a business card which is eye catching, and creative.

I am open to suggestions and any designs :)

Logo Design:

For our Logo Design we are looking for a bright, energetic logo, preferably a word logo which portrays strength and high intensity
If it has icon's etc in it thats fine again im open for suggestions :)
The Logo Design is for our Bootcamp which runs yearly
The bootcamp is called "Ferocity Drillcamp"

Target Market(s)

Age 20-40
Individuals who want to look great and have more energy

Industry/Entity Type

Business

Contact Information for Business Card

On the front
KT Prime Motion Doriel Maxton Personal Training / Bootcamps / Pilates / Nutrition Healthy mind, Healthy body, Ultimate lifestyle < our slogan
Icons for the following
Email:
Mobile:
Facebook:
Instagram:

On the back we would like to include somewhere
"Show this card to receive 50% off your first 30min pt session"
"Valid to one user only"

Logo Text

Ferocity Drillcamp

Font styles to use
Serif

Colors
e34197
0255a3
000000
ffffff

Requirements
Must have
• - Icons for instagram, facebook, email and mobile phone
• - Slogan: Healthy mind, Healthy body, Ultimate lifestyle
• - What we offer: Personal Training , Bootcamps, Pilates, Nutrition
• - Logo
• -
Nice to have
• - Our 50% offer on the back
• - a place for a photo
Should not have
• - Pink and Blue everywhere

```html
<!DOCTYPE html>
<html lang="en">
<head>
<meta charset="utf-8">
<title>KT Prime Motion – Business Card</title>
<link href="https://fonts.googleapis.com/css2?family=Bebas+Neue&family=Montserrat:wght@400;500;600;700;800&display=swap" rel="stylesheet">
<style>
  :root {
    --pink: #e34197;
    --blue: #0255a3;
    --black: #0a0a0a;
    --white: #ffffff;
    --ink: #1a1a1a;
    --grey: #555555;
    --stage: #3b312d;
    --faint: #1d1d1d;
    --photo-light: #c9a48c;
    --photo-dark: #2a2a2e;
  }
  * { margin: 0; padding: 0; box-sizing: border-box; }
  html, body { width: 1200px; height: 768px; overflow: hidden; }
  body {
    background: var(--stage);
    font-family: "Montserrat", sans-serif;
    position: relative;
  }
  .card {
    position: absolute;
    width: 540px;
    height: 309px;
    overflow: hidden;
    box-shadow: 0 14px 30px rgba(0,0,0,.45);
  }

  /* Back of card */
  .card-back {
    left: 60px;
    top: 70px;
    background: var(--black);
    color: var(--pink);
  }
  .card-back .faint-mark {
    position: absolute;
    left: 185px;
    top: 60px;
    width: 170px;
    height: 170px;
    border-radius: 50%;
    border: 22px solid var(--faint);
  }
  .card-back .offer {
    position: absolute;
    left: 30px;
    right: 30px;
    top: 56px;
    font-family: "Bebas Neue", sans-serif;
    font-size: 36px;
    line-height: 1.0;
    letter-spacing: 1px;
    text-align: center;
  }
  .card-back .terms {
    position: absolute;
    left: 0;
    right: 0;
    top: 160px;
    text-align: center;
    font-size: 11px;
    font-weight: 600;
    letter-spacing: 1px;
    text-transform: uppercase;
  }

  /* Front of card */
  .card-front {
    left: 600px;
    top: 390px;
    background: var(--white);
    color: var(--ink);
  }
  .brand {
    position: absolute;
    left: 18px;
    top: 36px;
    width: 250px;
    text-align: center;
  }
  .brand-dot {
    display: block;
    width: 62px;
    height: 62px;
    margin: 0 auto 10px;
    border-radius: 50%;
    border: 6px solid var(--pink);
  }
  .brand-name {
    font-size: 23px;
    font-weight: 800;
    color: var(--blue);
    line-height: 1;
    white-space: nowrap;
  }
  .brand-rule {
    height: 3px;
    background: var(--pink);
    margin: 7px 14px 6px;
  }
  .slogan {
    font-size: 9.5px;
    color: var(--grey);
    font-weight: 500;
    white-space: nowrap;
  }
  .person {
    position: absolute;
    left: 300px;
    top: 44px;
  }
  .person-name {
    font-size: 19px;
    font-weight: 700;
    letter-spacing: 1px;
    text-transform: uppercase;
  }
  .services {
    font-size: 10.5px;
    color: var(--grey);
    margin-top: 3px;
    line-height: 1.35;
    width: 200px;
  }
  .contacts {
    position: absolute;
    left: 300px;
    top: 116px;
    list-style: none;
  }
  .contacts li {
    display: flex;
    align-items: center;
    gap: 9px;
    font-size: 12px;
    line-height: 17px;
    white-space: nowrap;
  }
  .contacts svg { width: 11px; height: 11px; flex: none; }
  .contacts .square { width: 10px; height: 10px; background: var(--ink); border-radius: 2px; flex: none; }
  .bands { position: absolute; left: 0; bottom: 0; width: 540px; height: 80px; }
  .portrait {
    position: absolute;
    right: 0;
    bottom: 0;
    width: 140px;
    height: 112px;
    background: linear-gradient(180deg, var(--photo-light) 0%, #9c7a66 45%, var(--photo-dark) 75%);
  }
</style>
</head>
<body>

  <section class="card card-back">
    <div class="faint-mark" aria-hidden="true"></div>
    <p class="offer">Show this card to receive 50% off<br>your first 30min PT session</p>
    <p class="terms">Valid to one user only</p>
  </section>

  <section class="card card-front">
    <div class="brand">
      <span class="brand-dot" aria-hidden="true"></span>
      <div class="brand-name">KT PRIME MOTION</div>
      <div class="brand-rule"></div>
      <p class="slogan">Healthy mind, Healthy body, Ultimate lifestyle</p>
    </div>

    <div class="person">
      <h1 class="person-name">Doriel Maxton</h1>
      <p class="services">Personal Training , Bootcamps, Pilates, Nutrition</p>
    </div>

    <ul class="contacts">
      <li>
        <svg viewBox="0 0 12 12"><rect x="3" y="0.5" width="6" height="11" rx="1.2" fill="#1a1a1a"/><rect x="4" y="2" width="4" height="7" fill="#fff"/></svg>
        doriel@primemotionpt.com
      </li>
      <li>
        <svg viewBox="0 0 12 12"><rect x="0.5" y="2" width="11" height="8" fill="#1a1a1a"/><path d="M1 2.5 L6 6.5 L11 2.5" stroke="#fff" stroke-width="1" fill="none"/></svg>
        +00 555 481 2090
      </li>
      <li><span class="square"></span>facebook@dorielmaxton</li>
      <li><span class="square"></span>instagram@dorielmaxton</li>
    </ul>

    <svg class="bands" viewBox="0 0 540 80" aria-hidden="true">
      <polygon points="0,22 250,80 0,80" fill="var(--blue)"/>
      <polygon points="260,80 290,38 540,38 540,80" fill="var(--pink)"/>
    </svg>

    <div class="portrait" role="img" aria-label="Portrait photo of the trainer"></div>
  </section>

</body>
</html>
```